Sales Brochure- Generic Line Card 215mm x 140mm

Design a double-sided brochure similar to the attached sample. Cover Page contains a logo and theme that never changes. However, the background picture and the description text on the lower corner will be changed to advertise multiple services. Reverse-side contains Detailed Descriptive text related to the picture on Cover Page as well as Logo and Contact information for the business. Use the Ridgeline Controls website www.ridgelinecontrols.ca for theme, color and contact information. Also, use attached business card design for theme to match. Use the supplied logo. SIZE 215mm x 140mm

Font styles to use
Sans Serif

Colors

Designer to choose colors to be used in the design.

Requirements
Must have
• Look Similar to Sample Brochure but include Ridgeline Controls theme and colors

```html
<!DOCTYPE html>
<html lang="en">
<head>
<meta charset="utf-8">
<title>Ridgeline Controls – Line Card</title>
<link href="https://fonts.googleapis.com/css2?family=Open+Sans:wght@400;600&family=Lato:wght@400;700&display=swap" rel="stylesheet">
<style>
:root{
  --bg:#d9d9d9;
  --paper:#ffffff;
  --orange:#f04e0f;
  --teal:#0f8a80;
  --teal-dark:#0b4f4b;
  --panel:#262626;
  --ink:#1d1d1d;
  --muted:#e6e6e6;
  --ghost:#f6f6f6;
}
*{box-sizing:border-box;margin:0;padding:0}
html,body{width:1200px;height:1200px;overflow:hidden;background:var(--bg)}
body{position:relative;font-family:'Lato',sans-serif;color:var(--ink)}
.card{position:absolute;left:202px;width:798px;height:519px;background:var(--paper);overflow:hidden;box-shadow:4px 5px 8px rgba(0,0,0,.35)}
.card--front{top:48px}
.card--back{top:611px}

/* front */
.accent-bar{position:absolute;left:50px;top:0;width:38px;height:368px;background:var(--orange)}
.hero{position:absolute;left:91px;top:0;width:707px;height:408px}
.hero svg{display:block;width:100%;height:100%}
.brand{position:absolute;display:flex;align-items:center;gap:8px;font-family:'Lato',sans-serif;font-weight:700;color:var(--ink);letter-spacing:.3px;text-transform:uppercase;white-space:nowrap}
.brand__mark{width:20px;height:20px;background:var(--teal)}
.brand--front{left:52px;top:446px;font-size:19px}
.brand--back{left:566px;top:443px;font-size:15px}
.brand--back .brand__mark{width:18px;height:18px}
.product-title{position:absolute;left:582px;top:446px}
.product-title__rule{display:flex;height:2px;width:69px;margin:0 0 4px 3px}
.product-title__rule span{flex:1}
.product-title h1{font-family:'Open Sans',sans-serif;font-weight:400;font-size:24px;line-height:30px;color:var(--ink);white-space:nowrap}
.product-title h1 b{font-weight:600;color:var(--teal)}
.ghost{position:absolute;font-family:'Open Sans',sans-serif;font-size:48px;color:var(--ghost);white-space:nowrap;line-height:1}
.ghost--front{left:434px;top:476px}
.ghost--back{left:114px;top:477px;font-size:46px}

/* back */
.panel{position:absolute;left:90px;top:0;width:708px;height:365px;background:var(--panel);color:#f2f2f2}
.panel h2{position:absolute;left:33px;top:36px;font-family:'Open Sans',sans-serif;font-weight:400;font-size:19px}
.panel h2 b{font-weight:600}
.panel__body{position:absolute;left:34px;top:76px;width:612px;font-size:11.7px;line-height:14.3px}
.panel__body p{margin-bottom:8px}
.panel__note{position:absolute;left:34px;font-size:11.6px}
.panel__note--a{top:269px}
.panel__note--b{top:296px}
.panel__note--c{top:349px}
.stripe{position:absolute;left:90px;top:365px;width:708px;height:5px;display:flex}
.stripe span{flex:1}
.o{background:var(--orange)} .t{background:var(--teal)} .g{background:var(--muted)}
.contact{position:absolute;top:426px;font-size:11.5px;line-height:14px}
.contact--phones{left:95px}
.contact--address{left:291px}
.contact__row{display:flex;align-items:center;gap:7px}
.contact__row svg{width:14px;height:14px;flex:none}
.contact__phone{font-size:15.5px;line-height:18px;font-weight:700}
</style>
</head>
<body>

<section class="card card--front">
  <div class="accent-bar"></div>
  <div class="hero">
    <svg viewBox="0 0 707 408" preserveAspectRatio="none" role="img" aria-label="Close-up photo of stacked teal metal discs on industrial spindles">
      <defs>
        <linearGradient id="heroTone" x1="0" y1="0" x2="1" y2="0">
          <stop offset="0" stop-color="#0b4a47"/>
          <stop offset=".35" stop-color="#138680"/>
          <stop offset=".6" stop-color="#0b5651"/>
          <stop offset="1" stop-color="#0a3e3b"/>
        </linearGradient>
      </defs>
      <rect width="707" height="408" fill="url(#heroTone)"/>
      <rect width="77" height="368" fill="#f04e0f" opacity=".6"/>
      <polygon points="707,0 0,368 0,408 707,408" fill="#a6dcd6" opacity=".28"/>
    </svg>
  </div>
  <div class="brand brand--front"><span class="brand__mark"></span>Ridgeline Controls</div>
  <div class="product-title">
    <div class="product-title__rule"><span class="o"></span><span class="t"></span><span class="g"></span></div>
    <h1><b>Product</b> Name</h1>
  </div>
  <div class="ghost ghost--front">Product Name</div>
</section>

<section class="card card--back">
  <div class="panel">
    <h2><b>Product</b> Discription</h2>
    <div class="panel__body">
      <p>Lorem Ipsum is <b>simply dummy text</b> of the printing and typesetting industry. Lorem Ipsum has been the industry's standard dummy text ever since the 1500s, when an unknown printer took a galley of type and scrambled it to make a type specimen book. It has survived not only <b>five centuries</b>, but also the leap into electronic typesetting, remaining essentially unchanged. It was popularised in the 1960s with the release of Dryprint sheets containing Lorem Ipsum passages, and more recently with desktop publishing software like Pagecraft Studio including versions of Lorem Ipsum.</p>
      <p>Lorem Ipsum is simply dummy text of the printing and typesetting industry. Lorem Ipsum has been the industry's standard dummy text ever since the 1500s, when an unknown printer took a galley of type and scrambled it to make a type specimen book. It has survived not only five centuries, but also the leap into electronic typesetting, remaining essentially unchanged.</p>
    </div>
    <p class="panel__note panel__note--a">Lorem Ipsum is simply dummy text of the printing and typesetting industry.</p>
    <p class="panel__note panel__note--b">Lorem Ipsum is simply dummy text</p>
    <p class="panel__note panel__note--c">ISO9001</p>
  </div>
  <div class="stripe"><span class="o"></span><span class="t"></span><span class="g"></span></div>

  <div class="contact contact--phones">
    <div class="contact__row contact__phone">
      <svg viewBox="0 0 14 14"><circle cx="7" cy="7" r="7" fill="#f04e0f"/><path d="M4.6 3.6l1.4 1.5-.7 1a5 5 0 0 0 2.6 2.6l1-.7 1.5 1.4-.9 1.1C6.8 10.3 3.7 7.2 3.5 4.5z" fill="#fff"/></svg>
      780 555 0142
    </div>
    <div class="contact__row contact__phone">
      <svg viewBox="0 0 14 14"><circle cx="7" cy="7" r="7" fill="#f04e0f"/><rect x="4" y="4" width="6" height="6.5" rx=".8" fill="#fff"/><rect x="5" y="5" width="4" height="1.6" fill="#f04e0f"/></svg>
      888 555 0177
    </div>
    <div class="contact__row">
      <svg viewBox="0 0 14 14"><circle cx="7" cy="7" r="7" fill="#f04e0f"/><circle cx="7" cy="7" r="3.6" fill="none" stroke="#fff" stroke-width="1"/><path d="M3.4 7h7.2M7 3.4c-1.6 2-1.6 5.2 0 7.2M7 3.4c1.6 2 1.6 5.2 0 7.2" fill="none" stroke="#fff" stroke-width=".8"/></svg>
      www.ridgelinecontrols.ca
    </div>
  </div>

  <div class="contact contact--address">
    <div class="contact__row" style="align-items:flex-start">
      <svg viewBox="0 0 14 14"><circle cx="7" cy="7" r="7" fill="#f04e0f"/><path d="M7 3.2a2.6 2.6 0 0 0-2.6 2.6C4.4 7.8 7 10.8 7 10.8s2.6-3 2.6-5A2.6 2.6 0 0 0 7 3.2z" fill="#fff"/><circle cx="7" cy="5.8" r="1" fill="#f04e0f"/></svg>
      <span>4120 Millbrook Rd NW<br>Edmonton, AB<br>T6X 0R4</span>
    </div>
  </div>

  <div class="brand brand--back"><span class="brand__mark"></span>Ridgeline Controls</div>
  <div class="ghost ghost--back">Contact us</div>
</section>

</body>
</html>
```